Marketing and Outreach Collateral Template Design

We are a nonprofit that works with schools to provide advocacy and recently created a series of "Stand Up Guides" materials surrounding LGBTQ young people in schools. (The Northfield Bright Campus Coalition, a project of Civic Wellness Foundation of Lakeshore Counties, or CWFLC).We would like create a few items (wallet cards, magnets, postcards, etc.) that different bits of information on them, i.e. "top five things you need to know about [subject matter]" with our contact info and how to access the materials. We would provide raw files, copy, and a comprehensive list of the materials we are looking for to create. **What we need from you** would be a template for each of the 3-5 supplemental items that we want to build with copy language that we could manipulate in InDesign or Illustrator. We would like the templates to accompany the materials that already exist that were developed by one of our youth, but you would be able to make adjustments, offer ideas for polishing, etc. I've attached an example of one of our materials for your reference.

```html
<!DOCTYPE html>
<html lang="en">
<head>
<meta charset="utf-8">
<title>Stand Up Guides – Postcard Template</title>
<link rel="stylesheet" href="https://fonts.googleapis.com/css2?family=Montserrat:wght@600;800&family=Didact+Gothic&family=Alike&display=swap">
<style>
  :root {
    --sheet: #ffffff;
    --sheet-line: #222222;
    --card-sky: #dff0f5;
    --panel-mist: #c9e4e8;
    --sage: #d0dccb;
    --slate: #a9bcc2;
    --teal: #0f7ea8;
    --ink: #111111;
    --headline-white: #ffffff;
    --headline-ice: #c4e6ef;
    --rule: #3f6fa8;
  }
  * { box-sizing: border-box; margin: 0; padding: 0; }
  html, body { width: 848px; height: 1200px; overflow: hidden; background: var(--sheet); }
  .sheet {
    position: relative; width: 848px; height: 1200px;
    border: 2px solid var(--sheet-line); background: var(--sheet);
  }
  .sheet-label {
    position: absolute; left: 57px; top: 50px;
    font-family: "Alike", serif; font-size: 21px; color: var(--ink); letter-spacing: 0.5px;
  }
  .card {
    position: absolute; left: 56px; width: 733px; height: 498px;
    background: var(--card-sky); overflow: hidden;
  }
  .card--front { top: 97px; }
  .card--back { top: 636px; }
  .card-shapes { position: absolute; inset: 0; width: 100%; height: 100%; }

  .front-headline {
    position: absolute; left: 49px; top: 223px;
    font-family: "Montserrat", sans-serif; font-weight: 800;
    font-size: 47px; line-height: 51px; letter-spacing: 0.5px;
    text-transform: uppercase; color: var(--headline-white);
    text-shadow: 0 2px 14px rgba(0,0,0,0.45);
  }
  .front-headline .accent { display: block; color: var(--headline-ice); }

  .brand {
    position: absolute; left: 438px; display: flex; align-items: center; gap: 12px;
    width: 280px;
  }
  .card--front .brand { top: 392px; }
  .card--back .brand { top: 380px; }
  .brand-dot {
    flex: none; width: 40px; height: 40px; border-radius: 50%;
    border: 4px solid var(--teal);
  }
  .brand-name {
    font-family: "Montserrat", sans-serif; font-weight: 600;
    font-size: 19px; line-height: 23px; color: var(--teal);
  }

  .back-title {
    position: absolute; left: 31px; top: 88px;
    font-family: "Montserrat", sans-serif; font-weight: 600; font-size: 24px; color: var(--ink);
  }
  .back-title .accent { color: var(--teal); }
  .back-intro {
    position: absolute; left: 33px; top: 146px; width: 292px;
    font-family: "Didact Gothic", sans-serif; font-size: 14px; line-height: 24px; color: var(--ink);
  }
  .point-list { position: absolute; left: 31px; top: 242px; width: 262px; list-style: none; }
  .point-list li {
    position: relative; height: 39px; line-height: 39px; padding-left: 24px;
    font-family: "Alike", serif; font-size: 14px; color: var(--ink);
    white-space: nowrap; overflow: visible;
  }
  .point-list li::before {
    content: ""; position: absolute; left: 1px; top: 14px;
    width: 11px; height: 11px; border-radius: 50%; background: var(--teal);
  }
  .point-list li + li { border-top: 1px solid var(--rule); }

  .contact-box {
    position: absolute; left: 31px; top: 402px; width: 315px; height: 71px;
    background: var(--card-sky); border-radius: 5px; padding: 8px 0 0 22px;
    font-family: "Montserrat", sans-serif; color: var(--teal);
  }
  .contact-phone { font-weight: 600; font-size: 31px; line-height: 36px; white-space: nowrap; }
  .contact-note { font-size: 15px; line-height: 22px; white-space: nowrap; }
</style>
</head>
<body>
<div class="sheet">
  <p class="sheet-label">POST-CARD</p>

  <section class="card card--front">
    <svg class="card-shapes" viewBox="0 0 733 498" aria-hidden="true">
      <defs>
        <linearGradient id="artTone" x1="0" y1="0" x2="1" y2="1">
          <stop offset="0" stop-color="#dcebe2"/>
          <stop offset="0.55" stop-color="#9fb3c9"/>
          <stop offset="1" stop-color="#6d6f9e"/>
        </linearGradient>
      </defs>
      <circle cx="745" cy="18" r="72" fill="var(--teal)"/>
      <path d="M0 0 H505 C560 60 555 150 520 220 C470 320 380 360 360 430 C350 470 320 490 300 498 H0 Z"
            fill="#7d7aa8" opacity="0.55" transform="translate(8 4)"/>
    </svg>
    <svg class="card-shapes" viewBox="0 0 733 498" role="img"
         aria-label="Illustration area: four students and school staff standing together">
      <path d="M0 0 H505 C560 60 555 150 520 220 C470 320 380 360 360 430 C350 470 320 490 300 498 H0 Z"
            fill="url(#artTone)"/>
      <circle cx="40" cy="470" r="62" fill="var(--slate)"/>
    </svg>
    <h1 class="front-headline">Stand Up<br>Guides!<span class="accent">Law &amp;</span><span class="accent">Policy</span></h1>
    <div class="brand">
      <span class="brand-dot"></span>
      <span class="brand-name">Northfield Bright Campus Coalition</span>
    </div>
  </section>

  <section class="card card--back">
    <svg class="card-shapes" viewBox="0 0 733 498" aria-hidden="true">
      <path d="M0 0 H270 C330 40 360 140 420 230 C470 300 470 420 420 498 H0 Z" fill="var(--panel-mist)"/>
      <circle cx="35" cy="35" r="95" fill="var(--sage)"/>
      <path d="M85 498 C90 420 130 350 170 352 C215 355 230 440 240 498 Z" fill="var(--sage)"/>
      <rect x="0" y="402" width="85" height="96" fill="var(--slate)"/>
      <circle cx="760" cy="0" r="85" fill="var(--teal)"/>
      <circle cx="790" cy="305" r="95" fill="var(--teal)"/>
    </svg>
    <h2 class="back-title">Industry <span class="accent">Leader</span></h2>
    <p class="back-intro">Maecenas sed diam eget risus varius blandit sit amet ullamcorper nulla non metus auctor varius magna.</p>
    <ul class="point-list">
      <li>Pellentesque ornare sem lacinia quam</li>
      <li>Pellentesque ornare sem lacinia quam</li>
      <li>Pellentesque ornare sem lacinia quam</li>
    </ul>
    <div class="contact-box">
      <p class="contact-phone">+(1300)-245-671</p>
      <p class="contact-note">Call us for more information</p>
    </div>
    <div class="brand">
      <span class="brand-dot"></span>
      <span class="brand-name">Northfield Bright Campus Coalition</span>
    </div>
  </section>
</div>
</body>
</html>
```